Design our branded business card!

We'd love for you to design our business card and come up with a fitting design that reflects the Brimble brand. We're a growing tech startup with big ambitions. We've included our brand guidelines (contain colour palette), logo (EPS vector in CMYK) and old designs to help you on your way.

We'd like to keep the design fairly simple:

* Name
* Phone number
* Email address
* Website (www.brimble.life)
* Twitter (@brimble)
* Address (19 Fenwick Row, Leeds, UK, LS4 9QT).

This would need to include print and cutting marks.

If you have any questions just let us know!

Target Market(s)

Businesses, Press and our customers!

Industry/Entity Type

Business

Contact Information for Business Card

* Name
* Phone number
* Email address
* Twitter (@brimble)

Font styles to use
Sans Serif

Requirements
Must have
• 1. Must have the Brimble logo included.
• 2. Must use the font 'Brandon Text' in either 'light' or 'thin' (https://www.typevaultex.com/fonts/qrnfoundry/brandon-text/)
• 3. Must use exact colours references from the brand guidelines. Colours outside of the brand guidelines will be discounted. White (transparent) backgrounds are fine.
• 4. Must contain the following information:
• * Name
• * Phone number
• * Email address
• * Website (www.brimble.life)
• * Twitter (@brimble)
• * Address (19 Fenwick Row, Leeds, UK, LS4 9QT).
Nice to have
• Must use the font 'Brandon Text' in either 'light' or 'thin' (https://www.typevaultex.com/fonts/qrnfoundry/brandon-text/)
Should not have
• Colours outside of the brand guidelines will be discounted. White (transparent) backgrounds are fine.
• Avoid creating icons or including photography.

```html
<!DOCTYPE html>
<html lang="en">
<head>
<meta charset="utf-8">
<title>Brimble business card</title>
<link href="https://fonts.googleapis.com/css2?family=Questrial&display=swap" rel="stylesheet">
<style>
:root{
  --backdrop:#d6d6d8;
  --paper:#f4f4f3;
  --slate:#50545b;
  --leaf:#8bb55a;
  --ink:#3b3e43;
  --ink-soft:#6a6d72;
  --on-slate:#e9eaeb;
  --mark:#2b2d31;
}
*{margin:0;padding:0;box-sizing:border-box}
html,body{width:1200px;height:991px;overflow:hidden;background:var(--backdrop)}
body{position:relative;font-family:"Questrial",sans-serif;color:var(--ink)}

.sheet{position:absolute;left:290px;width:620px;height:424px}
.sheet-front{top:60px}
.sheet-back{top:507px}
.crop-marks{position:absolute;inset:0;width:620px;height:424px}
.crop-marks line{stroke:var(--mark);stroke-width:1}

.card{position:absolute;left:30px;top:30px;width:560px;height:364px;background:var(--paper)}
.card-back{background:var(--slate)}

.brand{position:absolute;left:50%;transform:translateX(-50%);display:flex;align-items:center;gap:.3em;white-space:nowrap;line-height:1;font-size:45px}
.brand-dot{width:1.3em;height:1.3em;border-radius:50%;background:var(--leaf);flex:none}
.brand-name{color:var(--ink)}
.card-back .brand-name{color:var(--on-slate)}
.card-front .brand{top:118px}
.card-back .brand{top:126px}

.card-holder{position:absolute;left:30px;top:252px;width:190px;text-align:right;font-size:15px;line-height:1.35;color:var(--ink-soft)}
.card-holder strong{display:block;font-weight:400;letter-spacing:.04em;color:var(--ink)}

.contact{position:absolute;left:236px;top:252px;display:flex;gap:14px;font-size:13px;line-height:1.4;color:var(--ink-soft);white-space:nowrap}
.contact .col + .col{border-left:1px solid #bbb;padding-left:14px}
.contact b{font-weight:400;color:var(--leaf)}

.card-back-url{position:absolute;width:100%;top:300px;text-align:center;font-size:15px;color:var(--on-slate)}
</style>
</head>
<body>

<section class="sheet sheet-front" aria-label="Business card, front, with crop marks">
  <div class="card card-front">
    <div class="brand"><span class="brand-dot"></span><span class="brand-name">brimble</span></div>
    <p class="card-holder"><strong>ELSA MARWOOD</strong>Marketing</p>
    <div class="contact">
      <div class="col"><b>T:</b> 0113 496 0321<br><b>E:</b> elsa@brimble.life<br><b>W:</b> www.brimble.life<br><b>Tw:</b> @brimble</div>
      <div class="col">19 Fenwick Row, Leeds<br>UK, LS4 9QT</div>
    </div>
  </div>
  <svg class="crop-marks" viewBox="0 0 620 424" aria-hidden="true">
    <line x1="2" y1="30" x2="22" y2="30"/><line x1="30" y1="2" x2="30" y2="22"/>
    <line x1="598" y1="30" x2="618" y2="30"/><line x1="590" y1="2" x2="590" y2="22"/>
    <line x1="2" y1="394" x2="22" y2="394"/><line x1="30" y1="402" x2="30" y2="422"/>
    <line x1="598" y1="394" x2="618" y2="394"/><line x1="590" y1="402" x2="590" y2="422"/>
  </svg>
</section>

<section class="sheet sheet-back" aria-label="Business card, back, with crop marks">
  <div class="card card-back">
    <div class="brand"><span class="brand-dot"></span><span class="brand-name">brimble</span></div>
    <p class="card-back-url">www.brimble.life</p>
  </div>
  <svg class="crop-marks" viewBox="0 0 620 424" aria-hidden="true">
    <line x1="2" y1="30" x2="22" y2="30"/><line x1="30" y1="2" x2="30" y2="22"/>
    <line x1="598" y1="30" x2="618" y2="30"/><line x1="590" y1="2" x2="590" y2="22"/>
    <line x1="2" y1="394" x2="22" y2="394"/><line x1="30" y1="402" x2="30" y2="422"/>
    <line x1="598" y1="394" x2="618" y2="394"/><line x1="590" y1="402" x2="590" y2="422"/>
  </svg>
</section>

</body>
</html>
```